Leeward Health Academy Open House

We need to create an advertisement for an upcoming open house that we are conducting. We can create a design in the dimensions of 10" (w) x 13.67" (h). Once that is approved, I will need the ad resized in the following dimensions:

8.5" (w) x 11" (h) - PDF
2400 pixels wide X 2400 pixels height - JPEG

Target Market(s)

Aspiring medical students

Industry/Entity Type

Medical

Requirements
Must have
• Logo
• Tag line: STUDY MEDICINE IN THE CARIBBEAN, BECOME A DOC IN THE US
• One of the attachments has a JPEG file with all the information to include in this new ad however the event location has changed to this:
• Sunday, April 22nd at 1pm at:
• Bramblewood Suites Chicago Quay Court
• 712 N. Fenwick Drive
• Chicago, IL 60687
• Event will be held on the 15th floor in The Osgood Room
• FREE parking. Refreshments will be served.
• Change email to admissions@lhamedic.org
• Use a nice background and creative design. The details of the event need to be big and emphasize OPEN HOUSE.

```html
<!DOCTYPE html>
<html lang="en">
<head>
<meta charset="utf-8">
<title>Leeward Health Academy – Open House</title>
<link href="https://fonts.googleapis.com/css2?family=Open+Sans:ital,wdth,wght@0,75..100,300..800;1,75..100,300..800&family=Oswald:wght@300;600&display=swap" rel="stylesheet">
<style>
  :root {
    --red: #d3222a;
    --red-dark: #b51c23;
    --navy: #1d2f5e;
    --blue-deep: #0f2a56;
    --blue-mid: #1f5aa6;
    --white: #ffffff;
    --ink: #2b3456;
  }
  * { margin: 0; padding: 0; box-sizing: border-box; }
  html, body { width: 927px; height: 1200px; overflow: hidden; }
  body {
    position: relative;
    font-family: "Open Sans", Arial, sans-serif;
    background: linear-gradient(180deg, var(--blue-mid) 55%, var(--blue-deep) 100%);
  }
  .top-bar { position: absolute; left: 0; top: 0; width: 927px; height: 22px; background: linear-gradient(90deg, var(--red-dark), var(--red)); }
  .bottom-bar { position: absolute; left: 0; top: 1178px; width: 927px; height: 22px; background: linear-gradient(90deg, var(--red-dark), var(--red)); }

  .title-block {
    position: absolute; left: 0; top: 22px; width: 333px; height: 202px;
    background: linear-gradient(135deg, var(--blue-deep), var(--blue-mid));
    color: var(--white); font-family: "Oswald", sans-serif; padding: 12px 0 0 40px;
  }
  .title-open { font-weight: 300; font-size: 80px; line-height: 82px; letter-spacing: -1px; transform: scaleX(0.92); transform-origin: left; }
  .title-house { font-weight: 600; font-size: 90px; line-height: 92px; letter-spacing: -1px; transform: scaleX(0.84); transform-origin: left; }

  .event-info { position: absolute; left: 333px; top: 22px; width: 594px; height: 202px; background: var(--white); padding: 10px 0 0 35px; }
  .event-date { color: var(--red); font-weight: 700; font-size: 37px; line-height: 48px; }
  .event-venue { color: var(--navy); font-size: 21px; line-height: 28px; margin-top: 6px; font-stretch: 92%; }
  .event-note { color: var(--red); font-size: 21px; margin-top: 10px; font-stretch: 92%; }

  .hero-photo {
    position: absolute; left: 0; top: 224px; width: 927px; height: 486px;
    background: radial-gradient(ellipse at 72% 45%, #6f99c9 0%, #3f6fae 40%, #24508e 75%, #1c437d 100%);
    border-bottom-right-radius: 36px;
  }
  .tagline {
    position: absolute; left: 40px; top: 300px; color: var(--white);
    font-weight: 700; font-size: 42px; line-height: 63px; font-stretch: 85%;
  }

  .brand-mark {
    position: absolute; left: 55px; top: 611px; width: 218px; height: 218px; border-radius: 50%;
    background: var(--white); display: flex; align-items: center; justify-content: center; text-align: center;
    color: var(--navy); font-weight: 700; font-size: 21px; line-height: 27px; padding: 30px;
  }

  .offer { position: absolute; left: 24px; top: 852px; width: 280px; text-align: center; color: var(--white); font-weight: 700; font-size: 19px; line-height: 38px; font-stretch: 92%; }
  .coupon {
    position: absolute; left: 71px; top: 974px; width: 185px; height: 37px; border-radius: 19px;
    background: var(--red); border: 2px solid var(--white); color: var(--white);
    font-weight: 800; font-size: 20px; letter-spacing: 3px; text-align: center; line-height: 33px;
  }

  .features {
    position: absolute; left: 333px; top: 698px; width: 594px; height: 393px; background: var(--white);
    border-top-left-radius: 40px; border-bottom-left-radius: 40px; list-style: none; padding: 36px 0 0 38px;
  }
  .feature { display: flex; align-items: center; color: var(--ink); font-size: 28px; height: 42px; font-stretch: 94%; }
  .feature svg { width: 22px; height: 22px; margin-right: 18px; flex: none; }
  .feature small { font-size: 19px; margin-left: 6px; }

  .rsvp { position: absolute; left: 24px; top: 1087px; color: var(--red); font-style: italic; font-weight: 700; font-size: 22px; }
  .contacts { position: absolute; left: 20px; top: 1128px; width: 890px; display: flex; justify-content: space-between; color: var(--white); font-size: 23px; }
  .contact { display: flex; align-items: center; gap: 10px; }
  .contact svg { width: 22px; height: 22px; }
</style>
</head>
<body>
  <div class="top-bar"></div>

  <header class="title-block">
    <div class="title-open">OPEN</div>
    <div class="title-house">HOUSE</div>
  </header>

  <section class="event-info">
    <p class="event-date">Sunday, April 22nd at 1pm</p>
    <p class="event-venue">Bramblewood Suites Chicago Quay Court<br>712 N. Fenwick Drive, Chicago, IL 60687<br>15th Floor, The Osgood Room</p>
    <p class="event-note">FREE parking. Refreshments will be served.</p>
  </section>

  <div class="hero-photo" role="img" aria-label="Photo of a smiling medical student in blue scrubs with a stethoscope and clipboard in a hospital corridor"></div>
  <h1 class="tagline">STUDY MEDICINE<br>IN THE CARIBBEAN,<br>BECOME A DOC<br>IN THE US</h1>

  <div class="brand-mark">Leeward Health Academy</div>

  <p class="offer">HAVE YOUR ENTIRE<br>APPLICATION FEE WAIVED!<br>ENTER COUPON CODE:</p>
  <div class="coupon">OPHUS</div>

  <ul class="features">
    <li class="feature"><svg viewBox="0 0 24 24"><circle cx="12" cy="12" r="9.5" fill="none" stroke="#d3222a" stroke-width="2"/><path d="M7.5 12.5l3 3 6-7" fill="none" stroke="#d3222a" stroke-width="2.4" stroke-linecap="round" stroke-linejoin="round"/></svg>4 Years MD Program</li>
    <li class="feature"><svg viewBox="0 0 24 24"><circle cx="12" cy="12" r="9.5" fill="none" stroke="#d3222a" stroke-width="2"/><path d="M7.5 12.5l3 3 6-7" fill="none" stroke="#d3222a" stroke-width="2.4" stroke-linecap="round" stroke-linejoin="round"/></svg>Financial Aid</li>
    <li class="feature"><svg viewBox="0 0 24 24"><circle cx="12" cy="12" r="9.5" fill="none" stroke="#d3222a" stroke-width="2"/><path d="M7.5 12.5l3 3 6-7" fill="none" stroke="#d3222a" stroke-width="2.4" stroke-linecap="round" stroke-linejoin="round"/></svg>Student Dorms</li>
    <li class="feature"><svg viewBox="0 0 24 24"><circle cx="12" cy="12" r="9.5" fill="none" stroke="#d3222a" stroke-width="2"/><path d="M7.5 12.5l3 3 6-7" fill="none" stroke="#d3222a" stroke-width="2.4" stroke-linecap="round" stroke-linejoin="round"/></svg>Modern Campus</li>
    <li class="feature"><svg viewBox="0 0 24 24"><circle cx="12" cy="12" r="9.5" fill="none" stroke="#d3222a" stroke-width="2"/><path d="M7.5 12.5l3 3 6-7" fill="none" stroke="#d3222a" stroke-width="2.4" stroke-linecap="round" stroke-linejoin="round"/></svg>Friendly Tution<small>($5,900/semester)</small></li>
    <li class="feature"><svg viewBox="0 0 24 24"><circle cx="12" cy="12" r="9.5" fill="none" stroke="#d3222a" stroke-width="2"/><path d="M7.5 12.5l3 3 6-7" fill="none" stroke="#d3222a" stroke-width="2.4" stroke-linecap="round" stroke-linejoin="round"/></svg>U.S Clinical Rotations</li>
    <li class="feature"><svg viewBox="0 0 24 24"><circle cx="12" cy="12" r="9.5" fill="none" stroke="#d3222a" stroke-width="2"/><path d="M7.5 12.5l3 3 6-7" fill="none" stroke="#d3222a" stroke-width="2.4" stroke-linecap="round" stroke-linejoin="round"/></svg>88.9% USMLE Passing Rate</li>
    <li class="feature"><svg viewBox="0 0 24 24"><circle cx="12" cy="12" r="9.5" fill="none" stroke="#d3222a" stroke-width="2"/><path d="M7.5 12.5l3 3 6-7" fill="none" stroke="#d3222a" stroke-width="2.4" stroke-linecap="round" stroke-linejoin="round"/></svg>Canadian Loans Available</li>
  </ul>

  <p class="rsvp">Please RSVP by email</p>
  <div class="contacts">
    <span class="contact"><svg viewBox="0 0 24 24"><circle cx="12" cy="12" r="11" fill="#d3222a"/><rect x="6" y="8" width="12" height="8" rx="1" fill="#fff"/><path d="M6.5 8.5l5.5 4 5.5-4" fill="none" stroke="#d3222a" stroke-width="1.3"/></svg>admissions@lhamedic.org</span>
    <span class="contact"><svg viewBox="0 0 24 24"><path d="M6.5 3.5l3 .5 1.2 4-2 1.5a11 11 0 0 0 5.8 5.8l1.5-2 4 1.2.5 3c-.3 1.6-1.6 2.5-3 2.5C10.5 20 4 13.5 4 6.5c0-1.4.9-2.7 2.5-3z" fill="none" stroke="#d3222a" stroke-width="2"/></svg>888-555-0142</span>
    <span class="contact"><svg viewBox="0 0 24 24"><circle cx="12" cy="12" r="11" fill="#d3222a"/><g fill="none" stroke="#fff" stroke-width="1.3"><circle cx="12" cy="12" r="6.5"/><ellipse cx="12" cy="12" rx="3" ry="6.5"/><path d="M5.5 12h13"/></g></svg>www.lhamedic.org</span>
  </div>

  <div class="bottom-bar"></div>
</body>
</html>
```